Engineering Consultant Business Card

I'm starting a new business as a high-end engineering consultant in a niche field. I've attached the jpg for my logo plus the branding guideline document that I've been following. You can see my business website here: www.tarvikworks.com
I'd like a business card that has the logo on one side, then the other side has (in any order): Tarvik Works, Inc.
Dana Whitlock
President and Chief EMC Engineer
www.tarvikworks.com
dana@tarvikworks.com
Optional: motto "We will solve your EMC problems as early as possible—ideally before they even start."
I'm not planning on including a phone number
Target Market(s)
Businesses, especially makers of electronics hardware
Industry/Entity Type
Electrical engineering
Contact Information for Business Card
Company name, my name, website, email

```html
<!DOCTYPE html>
<html lang="en">
<head>
<meta charset="utf-8">
<title>Tarvik Works, Inc. — Business Card</title>
<link rel="stylesheet" href="https://fonts.googleapis.com/css2?family=Roboto+Condensed:wght@400;700&display=swap">
<style>
  :root {
    --page: #2a2a2e;
    --card: #1e1e22;
    --card-deep: #141417;
    --blue: #2f47a6;
    --white: #f2f2f4;
    --gloss: #4a4a52;
    --pattern-mid: #26262b;
  }
  * { margin: 0; padding: 0; box-sizing: border-box; }
  html, body { width: 1200px; height: 780px; overflow: hidden; }
  body {
    background: var(--page);
    font-family: "Roboto Condensed", "Arial Narrow", sans-serif;
    position: relative;
  }
  .card {
    position: absolute;
    width: 560px;
    height: 320px;
    border-radius: 26px;
    background: var(--card);
    border: 3px solid var(--blue);
    border-top-color: transparent;
    border-left-color: transparent;
    overflow: hidden;
  }
  .card-back { left: 40px; top: 50px; }
  .card-front { left: 600px; top: 410px; }

  /* back side */
  .back-pattern {
    position: absolute; inset: 0;
    background:
      radial-gradient(ellipse 70% 45% at 45% 8%, var(--gloss) 0%, transparent 70%),
      repeating-linear-gradient(0deg, var(--pattern-mid) 0 14px, var(--card) 14px 28px),
      linear-gradient(160deg, var(--card) 0%, var(--card-deep) 100%);
    background-blend-mode: screen, normal, normal;
    opacity: 0.95;
  }
  .back-accent {
    position: absolute;
    left: 384px; top: 150px;
    display: flex; align-items: center; gap: 6px;
    color: var(--blue);
    font-weight: 700;
    font-size: 12px;
    line-height: 1;
  }
  .back-accent-dot {
    width: 14px; height: 14px;
    border-radius: 50%;
    background: var(--blue);
  }

  /* front side */
  .brand {
    position: absolute;
    left: 34px; top: 96px;
    width: 220px;
    display: flex; align-items: center; gap: 12px;
    color: var(--blue);
    font-weight: 700;
    font-size: 30px;
    line-height: 1.05;
  }
  .brand-dot {
    flex: none;
    width: 48px; height: 48px;
    border-radius: 50%;
    background: var(--blue);
  }
  .divider {
    position: absolute;
    left: 272px; top: 60px;
    width: 1.5px; height: 120px;
    background: var(--white);
  }
  .contact {
    position: absolute;
    left: 298px; top: 56px;
    color: var(--white);
  }
  .contact-name {
    color: var(--blue);
    font-weight: 700;
    font-size: 34px;
    line-height: 1;
  }
  .contact-title {
    font-size: 15px;
    margin-top: 4px;
  }
  .contact-list {
    list-style: none;
    margin-top: 18px;
    font-size: 14px;
  }
  .contact-list li {
    display: flex; align-items: center; gap: 8px;
    margin-bottom: 6px;
  }
  .contact-list svg { width: 14px; height: 14px; flex: none; }
  .motto {
    position: absolute;
    left: 34px; right: 24px; bottom: 50px;
    color: var(--white);
    font-size: 14.5px;
  }
  .band {
    position: absolute;
    left: 0; right: 0; bottom: 18px;
    height: 18px;
    background: var(--blue);
  }
</style>
</head>
<body>
  <section class="card card-back">
    <div class="back-pattern" role="img" aria-label="Repeating pattern of the company mark, glossy black on black with a soft sheen at the top"></div>
    <div class="back-accent">
      <span class="back-accent-dot"></span>
      <span>Tarvik Works, Inc.</span>
    </div>
  </section>

  <section class="card card-front">
    <div class="brand">
      <span class="brand-dot"></span>
      <span class="brand-name">Tarvik Works, Inc.</span>
    </div>
    <div class="divider"></div>
    <div class="contact">
      <h1 class="contact-name">Dana Whitlock</h1>
      <p class="contact-title">President and Chief EMC Engineer</p>
      <ul class="contact-list">
        <li>
          <svg viewBox="0 0 16 16" fill="none" stroke="#2f47a6" stroke-width="1.6"><circle cx="8" cy="8" r="6.5"/><path d="M1.5 8h13M8 1.5c2.2 2 2.2 11 0 13M8 1.5c-2.2 2-2.2 11 0 13"/></svg>
          <span>www.tarvikworks.com</span>
        </li>
        <li>
          <svg viewBox="0 0 16 16" fill="none" stroke="#2f47a6" stroke-width="1.6"><rect x="1.5" y="3.5" width="13" height="9" rx="1"/><path d="M1.5 4l6.5 5 6.5-5"/></svg>
          <span>dana@tarvikworks.com</span>
        </li>
      </ul>
    </div>
    <p class="motto">We will solve your EMC problems as early as possible—ideally before they even start</p>
    <div class="band"></div>
  </section>
</body>
</html>
```